Website re-design wedding music business

I need my wordpress wedding music website redesigned. I'm a wedding pianist and also provide duo/trio entertainment with other musicians and looking for an overhaul of my wordpress site.

Website: tomaslevett.com.au

Target Market(s)

brides; engaged couples

Industry/Entity Type

Wedding

Number of Pages Required

5+ page

Colors

Designer to choose colors to be used in the design.

Requirements
Must have
• I'm looking to overhaul my website which is looking rather tired after 4 years. It is functional but not inviting to visitors. Initially my website started out as a solo piano player providing music for wedding. It is gradually growing now where brides can book
• 1) Solo Piano
• 2) Duo (any combination of Piano / Cello / Vocalist / Violin)
• 3) Trio (any combination of Piano/ Cello /Vocalist / Violin)
• in future it may increase to 4 / 5 /6 piece bands so that needs to be taken into account for the future growth where I'll recruit other musicians.
• Some other functionality I'd like to see
• - Visitors want a calendar to know availability of musicians
• - Automatically providing enquiry price & discount (if applicable)
• - Automating the booking form process (manual) - There's a PDF form I send to the customer after we go back/forth on email on songs/price etc but if more of it could be automated online that would be great. If move to online it would be good to be able to override the set prices with a custom price and also providing a payment gateway
• More Flexibility on pricing - customer selects type of artists they want and it calculates a price based on who they have chosen whether it is a ceremony or canapes or reception (or combination of any). Extra transport fee is added if >50km out of Melbourne.
• How would you re-design this website. Imagine you are a bride/groom looking to book wedding music services. I would love to see some concepts .
• Please indicate any other fees required for your submission and level of support post this competition. I would like this to be an on-going relationship.
Nice to have
• I'd preferably like the website to be in wordpress as I've been familiar with it over time and can do basic updates in the back end. Happy for other suggestions if you can convince me I should move away from wordpress.

```html
<!DOCTYPE html>
<html lang="en">
<head>
<meta charset="utf-8">
<title>Tomas Levett – Wedding Pianist</title>
<link rel="stylesheet" href="https://fonts.googleapis.com/css2?family=Questrial&family=Great+Vibes&display=swap">
<style>
:root{
  --rose:#ac5e50;
  --rose-soft:#f3e7e4;
  --sage:#98a36b;
  --ink:#333333;
  --charcoal:#3c3c3c;
  --line:#d9d9d9;
  --white:#ffffff;
  --night:#2b2b2b;
}
*{box-sizing:border-box;margin:0;padding:0}
html,body{width:1200px;height:3863px;overflow:hidden}
body{font-family:"Questrial",sans-serif;color:var(--ink);background:var(--white);position:relative}
.abs{position:absolute}
.btn{position:absolute;display:flex;align-items:center;justify-content:center;border-radius:40px;font-size:15px;letter-spacing:.5px;text-transform:uppercase}
.btn-outline-light{border:2px solid var(--white);color:var(--white)}
.btn-outline-rose{border:2px solid var(--rose);color:var(--rose);font-size:12px}
.btn-rose{background:var(--rose);color:var(--white)}

/* header */
.site-header{left:0;top:0;width:1200px;height:95px;background:var(--white)}
.brand{display:flex;align-items:center;gap:10px}
.brand-dot{width:58px;height:58px;border-radius:50%;background:#111}
.brand-name{font-size:24px;color:#222;letter-spacing:.5px}
.badge{position:absolute;top:20px;width:52px;height:52px;border-radius:50%}
.search{left:837px;top:48px;width:275px;height:34px;border:1.5px solid #bbb;border-radius:20px;font-size:12px;color:#888;padding:9px 18px}
.social{position:absolute;top:10px;width:16px;height:16px;border-radius:50%;background:#222}

.main-nav{left:0;top:95px;width:1200px;height:47px;background:var(--rose);display:flex;align-items:center;padding-left:84px}
.main-nav span{color:var(--white);font-size:13px;text-transform:uppercase;padding:0 16px}

/* hero */
.hero{left:0;top:155px;width:1200px;height:561px;background:linear-gradient(90deg,#231d1b 0%,#4f4441 30%,#9a8680 52%,#c9a39a 68%,#e7dfdb 100%)}
.hero-title{left:88px;top:315px;font-family:"Great Vibes",cursive;font-size:78px;line-height:90px;color:var(--white)}
.hero-sub{left:88px;top:432px;font-size:25px;color:var(--white)}

/* intro */
.intro{left:0;top:726px;width:1200px;height:324px;background:var(--sage)}
.intro p{position:absolute;left:85px;top:22px;width:1030px;text-align:center;color:var(--white);font-size:17px;line-height:34px}

/* ensembles */
.ensemble{position:absolute;width:300px;text-align:center}
.ensemble-icon{width:170px;height:170px;border-radius:50%;background:var(--rose);border:6px solid var(--rose-soft);margin:0 auto;display:flex;align-items:center;justify-content:center}
.ensemble h3{font-weight:400;font-size:25px;margin-top:30px;color:#222}

/* gallery */
.gallery-tile{position:absolute;width:324px;height:211px}

/* packages */
.packages{left:0;top:1818px;width:1200px;height:453px;background:var(--rose)}
.packages h2{position:absolute;top:55px;width:1200px;text-align:center;font-weight:400;font-size:33px;color:var(--white)}
.packages .rule{position:absolute;left:570px;top:110px;width:60px;height:1px;background:#d79a8e}
.packages p{position:absolute;left:330px;top:132px;width:540px;text-align:center;color:#f1d5cf;font-size:15px;line-height:28px}
.card{position:absolute;top:2045px;width:328px;height:375px;background:var(--white);border:1px solid #e2e2e2;text-align:center}
.card-head{height:46px;background:var(--charcoal);color:var(--white);font-size:19px;text-transform:uppercase;line-height:46px}
.card-pennant{position:absolute;left:60px;top:45px;width:208px;height:86px}
.card-price{position:absolute;left:0;top:50px;width:328px;font-size:40px;color:var(--white)}
.card-city{position:absolute;top:170px;width:328px;font-size:18px}
.card-rule{position:absolute;left:0;top:212px;width:328px;height:1px;background:var(--line)}
.card-time{position:absolute;top:224px;width:328px;font-size:18px}
.card .btn{left:67px;top:297px;width:194px;height:50px;font-size:17px}
.slide-arrow{position:absolute;top:2186px;width:52px;height:52px;border-radius:50%;border:2px solid rgba(255,255,255,.45);display:flex;align-items:center;justify-content:center}

/* testimonial */
.testimonial{left:0;top:2487px;width:1200px;height:186px;background:var(--sage);text-align:center;color:var(--white)}
.testimonial .quote{position:absolute;left:340px;top:36px;width:520px;font-size:16px;line-height:26px}
.testimonial .name{position:absolute;top:103px;width:1200px;font-size:20px;letter-spacing:1px}
.testimonial .place{position:absolute;top:133px;width:1200px;font-size:13px;letter-spacing:.5px}

/* events */
.events-photo{left:85px;top:2745px;width:353px;height:152px}
.calendar{left:85px;top:2920px;width:353px;height:227px;background:#ececec}
.cal-head{height:62px;background:var(--rose);color:var(--white);font-size:27px;padding:14px 12px;display:flex;justify-content:space-between}
.cal-grid{display:grid;grid-template-columns:repeat(7,43px);gap:5px;padding:6px 12px}
.cal-grid span{height:22px;font-size:17px;color:#777;text-align:center;line-height:22px}
.cal-grid .dow{font-size:9px;height:14px;line-height:14px;color:#999}
.cal-grid .day{background:#c9c9c9;color:#666}
.events-divider{left:494px;top:2815px;width:1px;height:310px;background:var(--line)}
.events-title{left:572px;top:2738px;font-size:36px;color:#333}
.dots{left:1071px;top:2759px;display:flex;gap:5px}
.dots span{width:8px;height:8px;border-radius:50%;background:#ccc}
.dots span.on{background:var(--rose)}
.event{position:absolute;left:572px;width:540px;height:101px;border:1px solid #ddd;background:var(--white)}
.event-thumb{position:absolute;left:18px;top:23px;width:100px;height:56px;background:linear-gradient(135deg,#3a2c26,#a08a78)}
.event h4{position:absolute;left:135px;top:28px;font-size:12px;font-weight:700;font-family:Arial,sans-serif}
.event p{position:absolute;left:135px;top:48px;width:330px;font-size:11px;line-height:15px;font-family:Arial,sans-serif;color:#444}
.event-date{position:absolute;right:0;top:0;width:51px;height:55px;background:var(--rose);color:var(--white);text-align:center}
.event-date b{display:block;font-size:26px;font-weight:400;line-height:34px}
.event-date small{font-size:11px}

/* contact */
.contact{left:0;top:3208px;width:1200px;height:397px;background:linear-gradient(180deg,#fafafa 0%,#ececec 100%);overflow:hidden}
.contact-flowers{position:absolute}
.contact h2{position:absolute;top:58px;width:1200px;text-align:center;font-weight:400;font-size:26px;color:#333}
.contact .rule{position:absolute;left:575px;top:98px;width:50px;height:1px;background:#caa}
.field{position:absolute;border-bottom:1.5px solid #555;font-size:11px;color:#333;padding-bottom:4px}
.contact .btn{left:528px;top:332px;width:142px;height:40px;font-size:18px;text-transform:none}

/* footer */
.site-footer{left:0;top:3610px;width:1200px;height:196px;background:var(--sage)}
.site-footer .brand{position:absolute;left:462px;top:36px}
.foot-nav{position:absolute;top:152px;width:1200px;display:flex;justify-content:center}
.foot-nav span{color:var(--white);font-size:11px;text-transform:uppercase;padding:0 15px}
.copyright{left:0;top:3806px;width:1200px;height:57px;background:var(--night);color:#999;font-size:11px;text-align:center;line-height:57px}
</style>
</head>
<body>

<header class="abs site-header">
  <div class="abs brand" style="left:88px;top:17px">
    <div class="brand-dot"></div>
    <span class="brand-name">TOMASLEVETT</span>
  </div>
  <div class="badge" style="left:512px;background:#2e2e2e"></div>
  <div class="badge" style="left:578px;background:#b89a3e"></div>
  <div class="badge" style="left:645px;background:#d2d6dc"></div>
  <span class="social" style="left:993px"></span>
  <span class="social" style="left:1025px"></span>
  <span class="social" style="left:1057px"></span>
  <span class="social" style="left:1089px;border-radius:3px"></span>
  <div class="abs search">Search...</div>
</header>

<nav class="abs main-nav">
  <span>Home</span><span>About Tomas</span><span>Events</span><span>Music Video</span><span>Repertoire</span><span>Prices</span><span>Gallery</span><span>Testimonials</span><span>Buy CD</span><span>FAQs</span><span>Contact</span>
</nav>

<section class="abs hero" role="img" aria-label="Red rose resting on piano keys"></section>
<div class="abs hero-title">Tomas Levett ...</div>
<div class="abs hero-sub">Wedding Pianist &nbsp;|&nbsp; Event Pianist</div>
<div class="btn btn-outline-light" style="left:88px;top:505px;width:234px;height:60px;font-size:19px">Contact Us</div>

<section class="abs intro">
  <p>Lorem Ipsum is simply dummy text of the printing and typesetting industry. Lorem Ipsum has been the industry's standard dummy text ever since the 1500s, when an unknown printer took a galley of type and scrambled it to make a type specimen book. It has survived not only five centuries, but also the leap into electronic typesetting.</p>
  <div class="btn btn-outline-light" style="left:479px;top:144px;width:240px;height:62px;font-size:17px">Book Now</div>
</section>

<svg width="0" height="0" style="position:absolute">
  <symbol id="keys" viewBox="0 0 80 56">
    <rect x="2" y="2" width="76" height="52" rx="3" fill="none" stroke="#fff" stroke-width="3"/>
    <line x1="2" y1="18" x2="78" y2="18" stroke="#fff" stroke-width="3"/>
    <g stroke="#fff" stroke-width="2.5"><line x1="14" y1="18" x2="14" y2="54"/><line x1="26" y1="18" x2="26" y2="54"/><line x1="38" y1="18" x2="38" y2="54"/><line x1="50" y1="18" x2="50" y2="54"/><line x1="62" y1="18" x2="62" y2="54"/></g>
    <g fill="#fff"><rect x="11" y="18" width="6" height="20"/><rect x="23" y="18" width="6" height="20"/><rect x="47" y="18" width="6" height="20"/><rect x="59" y="18" width="6" height="20"/></g>
    <g fill="#fff"><circle cx="54" cy="10" r="2"/><circle cx="62" cy="10" r="2"/><circle cx="70" cy="10" r="2"/></g>
  </symbol>
</svg>

<div class="ensemble" style="left:100px;top:965px">
  <div class="ensemble-icon"><svg width="84" height="60"><use href="#keys"/></svg></div>
  <h3>SOLO PIANO</h3>
</div>
<div class="btn btn-outline-rose" style="left:175px;top:1210px;width:150px;height:44px">Book Now</div>

<div class="ensemble" style="left:450px;top:965px">
  <div class="ensemble-icon"><svg width="84" height="60"><use href="#keys"/></svg></div>
  <h3>DUO</h3>
</div>
<div class="btn btn-outline-rose" style="left:525px;top:1210px;width:150px;height:44px">Book Now</div>

<div class="ensemble" style="left:800px;top:965px">
  <div class="ensemble-icon"><svg width="84" height="60"><use href="#keys"/></svg></div>
  <h3>TRIO</h3>
</div>
<div class="btn btn-outline-rose" style="left:875px;top:1210px;width:150px;height:44px">Book Now</div>

<div class="gallery-tile" style="left:88px;top:1303px;background:linear-gradient(135deg,#3b2418,#8a5a3a 60%,#d9cbb8)" role="img" aria-label="Pianist at a grand piano beside a bride in a hall"></div>
<div class="gallery-tile" style="left:438px;top:1303px;background:linear-gradient(135deg,#cfc6bb,#f2eee8 50%,#2a2624)" role="img" aria-label="Sheet music resting on piano keys"></div>
<div class="gallery-tile" style="left:788px;top:1303px;background:linear-gradient(135deg,#0f0d0c,#3a2f29 55%,#c2b3a4)" role="img" aria-label="Hands playing piano keys"></div>
<div class="gallery-tile" style="left:88px;top:1540px;background:linear-gradient(135deg,#141414,#c3292a 55%,#eeeeee)" role="img" aria-label="Red rose and wedding rings on a keyboard"></div>
<div class="gallery-tile" style="left:438px;top:1540px;background:linear-gradient(135deg,#2a2a2a,#d8c4b4 50%,#f4f1ec)" role="img" aria-label="Couple's hands together on piano keys"></div>
<div class="gallery-tile" style="left:788px;top:1540px;background:linear-gradient(135deg,#e9e3d6,#f6efe0 50%,#c7b08a)" role="img" aria-label="White rose on sheet music and keys"></div>

<section class="abs packages">
  <h2>OUR PACKAGES</h2>
  <div class="rule"></div>
  <p>It is a long established fact that a reader will be distracted by the readable content of a page when looking at its layout.</p>
</section>
<div class="slide-arrow" style="left:10px"><svg width="14" height="20"><path d="M11 2 3 10l8 8" stroke="#fff" stroke-width="2" fill="none"/></svg></div>
<div class="slide-arrow" style="left:1138px;border-color:#ddd"><svg width="14" height="20"><path d="M3 2l8 8-8 8" stroke="#bbb" stroke-width="2" fill="none"/></svg></div>

<div class="card" style="left:85px">
  <div class="card-head">Wedding Ceremony</div>
  <svg class="card-pennant" viewBox="0 0 208 86"><path d="M0 0h208v40l-104 46L0 40z" fill="#3c3c3c"/></svg>
  <div class="card-price">$300</div>
  <div class="card-city">Melbourne</div>
  <div class="card-rule"></div>
  <div class="card-time">1 Hour(s)</div>
  <div class="btn btn-rose">Book Now</div>
</div>
<div class="card" style="left:436px">
  <div class="card-head">Wedding Ceremony</div>
  <svg class="card-pennant" viewBox="0 0 208 86"><path d="M0 0h208v40l-104 46L0 40z" fill="#3c3c3c"/></svg>
  <div class="card-price">$300</div>
  <div class="card-city">Melbourne</div>
  <div class="card-rule"></div>
  <div class="card-time">1 Hour(s)</div>
  <div class="btn btn-rose">Book Now</div>
</div>
<div class="card" style="left:787px">
  <div class="card-head">Wedding Ceremony</div>
  <svg class="card-pennant" viewBox="0 0 208 86"><path d="M0 0h208v40l-104 46L0 40z" fill="#3c3c3c"/></svg>
  <div class="card-price">$300</div>
  <div class="card-city">Melbourne</div>
  <div class="card-rule"></div>
  <div class="card-time">1 Hour(s)</div>
  <div class="btn btn-rose">Book Now</div>
</div>

<section class="abs testimonial">
  <svg class="abs" style="left:222px;top:25px" width="90" height="70" viewBox="0 0 90 70"><g fill="rgba(255,255,255,.18)"><path d="M4 70V40C4 18 16 6 38 2v12C26 18 22 26 22 36h16v34z"/><path d="M50 70V40C50 18 62 6 84 2v12C72 18 68 26 68 36h16v34z"/></g></svg>
  <svg class="abs" style="left:840px;top:98px" width="90" height="70" viewBox="0 0 90 70"><g fill="rgba(255,255,255,.18)" transform="rotate(180 45 35)"><path d="M4 70V40C4 18 16 6 38 2v12C26 18 22 26 22 36h16v34z"/><path d="M50 70V40C50 18 62 6 84 2v12C72 18 68 26 68 36h16v34z"/></g></svg>
  <div class="quote">I would work with him again in a second! So easy to work with and got back to me super quick!</div>
  <div class="name">CARLA WHITMORE</div>
  <div class="place">(HOBART, AUSTRALIA)</div>
  <svg class="abs" style="left:14px;top:70px" width="30" height="30"><circle cx="15" cy="15" r="13" fill="none" stroke="rgba(255,255,255,.3)" stroke-width="1.5"/></svg>
  <svg class="abs" style="left:1156px;top:70px" width="30" height="30"><circle cx="15" cy="15" r="13" fill="none" stroke="rgba(255,255,255,.3)" stroke-width="1.5"/></svg>
</section>

<div class="abs events-photo" role="img" aria-label="White rose lying on piano keys" style="background:linear-gradient(160deg,#f4ede0,#e8d9bc 50%,#6b5b45)"></div>
<div class="abs calendar">
  <div class="cal-head"><span>March 2017</span><span style="font-size:18px;color:#e7bdb5">&lsaquo;&nbsp;&nbsp;&rsaquo;</span></div>
  <div class="cal-grid">
    <span class="dow">Mon</span><span class="dow">Tue</span><span class="dow">Wed</span><span class="dow">Thr</span><span class="dow">Fri</span><span class="dow">Sat</span><span class="dow">Sun</span>
    <span></span><span></span><span class="day">1</span><span class="day">2</span><span class="day">3</span><span class="day">4</span><span class="day">5</span>
    <span class="day">6</span><span class="day">7</span><span class="day">8</span><span class="day">9</span><span class="day">10</span><span class="day">11</span><span class="day">12</span>
    <span class="day">13</span><span class="day">14</span><span class="day">15</span><span class="day">16</span><span class="day">17</span><span class="day">18</span><span class="day">19</span>
    <span class="day">20</span><span class="day">21</span><span class="day">22</span><span class="day">23</span><span class="day">24</span><span class="day">25</span><span class="day">26</span>
    <span class="day">27</span><span class="day">28</span>
  </div>
</div>
<div class="abs events-divider"></div>
<div class="abs events-title">Upcoming events</div>
<div class="abs dots"><span></span><span class="on"></span><span></span></div>

<div class="event" style="top:2799px">
  <div class="event-thumb" role="img" aria-label="Pianist performing at an event"></div>
  <h4>Lorem ipsum dolor</h4>
  <p>It is a long established fact that a reader will be distracted by the readable content of a page when looking at its layout.</p>
  <div class="event-date"><b>23</b><small>may</small></div>
</div>
<div class="event" style="top:2920px">
  <div class="event-thumb" role="img" aria-label="Pianist performing at an event"></div>
  <h4>Lorem ipsum dolor</h4>
  <p>It is a long established fact that a reader will be distracted by the readable content of a page when looking at its layout.</p>
  <div class="event-date"><b>03</b><small>june</small></div>
</div>
<div class="event" style="top:3041px">
  <div class="event-thumb" role="img" aria-label="Pianist performing at an event"></div>
  <h4>Lorem ipsum dolor</h4>
  <p>It is a long established fact that a reader will be distracted by the readable content of a page when looking at its layout.</p>
  <div class="event-date"><b>30</b><small>may</small></div>
</div>

<section class="abs contact">
  <div class="contact-flowers" style="left:0;top:172px;width:300px;height:225px;background:linear-gradient(90deg,#dfe2cc 0%,rgba(236,236,236,0) 100%)" role="img" aria-label="Pale hellebore flowers"></div>
  <div class="contact-flowers" style="left:300px;top:262px;width:560px;height:135px;background:linear-gradient(180deg,rgba(236,236,236,0) 0%,#efd8d3 100%)" role="img" aria-label="Pink roses and green leaves"></div>
  <div class="contact-flowers" style="left:860px;top:172px;width:340px;height:225px;background:linear-gradient(270deg,#e2e5cf 0%,rgba(236,236,236,0) 100%)" role="img" aria-label="White flowers and leaves"></div>
  <h2>CONTACT US</h2>
  <div class="rule"></div>
  <div class="field" style="left:180px;top:164px;width:193px">Name*</div>
  <div class="field" style="left:502px;top:164px;width:193px">Email*</div>
  <div class="field" style="left:824px;top:164px;width:193px">Phone*</div>
  <div class="field" style="left:180px;top:248px;width:837px;height:36px">Message</div>
  <div class="btn btn-rose">Submit</div>
</section>

<footer class="abs site-footer">
  <div class="brand">
    <div class="brand-dot" style="width:74px;height:74px"></div>
    <span class="brand-name" style="font-size:26px">TOMASLEVETT</span>
  </div>
  <div class="foot-nav">
    <span>Home</span><span>About Tomas</span><span>Events</span><span>Music Video</span><span>Repertoire</span><span>Prices</span><span>Gallery</span><span>Testimonials</span><span>Buy CD</span><span>FAQs</span><span>Contact</span>
  </div>
</footer>
<div class="abs copyright">tomaslevett.com.au © 2017. All rights reserved</div>

</body>
</html>
```